Volora Laundry and Dry Cleaning Poster

We need a Poster and Window Sticker for our Laundry and Dry cleaning shop (VOLORA LAUNDRY AND DRY CLEANING).
info we like on the design. Logo is included
Company Name: Volora Laundry and Dry Cleaning
Slogan: It Comes Back Clean
Location: Kwentu-Dasor, Accra
Working Hours: Mon-Sat 8am to 5pm
Tel: +233 30 781 6242
email:info@voloralaundry.example
website: www.voloralaundry.example
fb: fb.com/voloralaundry

Target Market(s)

Laundry Shop

Colors
33a6d7
9bcb3b

```html
<!DOCTYPE html>
<html lang="en">
<head>
<meta charset="utf-8">
<title>Volora Laundry and Dry Cleaning – Poster</title>
<link rel="stylesheet" href="https://fonts.googleapis.com/css2?family=Open+Sans:wght@400;600;700;800&family=Fira+Sans+Condensed:ital,wght@1,600&display=swap">
<style>
  :root {
    --brand-blue: #33a6d7;
    --box-blue: #1e8bcb;
    --brand-green: #9bcb3b;
    --white: #ffffff;
    --photo-dark: #2a2826;
    --photo-mid: #55514d;
  }
  * { margin: 0; padding: 0; box-sizing: border-box; }
  html, body { width: 1019px; height: 1200px; overflow: hidden; background: var(--white); }
  .poster {
    position: relative; width: 1019px; height: 1200px;
    background: var(--white); font-family: "Open Sans", sans-serif; overflow: hidden;
  }
  .brand {
    position: absolute; top: 30px; left: 0; width: 100%;
    display: flex; justify-content: center; align-items: center; gap: 16px;
    color: var(--brand-blue); font-weight: 700;
  }
  .brand-dot { width: 120px; height: 120px; border-radius: 50%; background: var(--brand-blue); }
  .brand-name { display: flex; flex-direction: column; line-height: 1; }
  .brand-name .word { font-size: 92px; letter-spacing: -1px; }
  .brand-name .sub { font-size: 17px; letter-spacing: 0.2px; margin-top: 6px; padding-left: 4px; }

  .rule-green { position: absolute; top: 231px; left: 0; width: 100%; height: 11px; background: var(--brand-green); }
  .slogan {
    position: absolute; top: 182px; left: 250px; width: 577px; height: 100px;
    background: var(--brand-green); border-radius: 20px;
    display: flex; align-items: center; justify-content: center;
    color: var(--white); font-family: "Fira Sans Condensed", sans-serif;
    font-style: italic; font-weight: 600; font-size: 46px; letter-spacing: 2.5px;
  }
  .photo {
    position: absolute; top: 242px; left: 0; width: 100%; height: 686px;
    background: radial-gradient(ellipse at 42% 55%, var(--photo-mid) 0%, var(--photo-dark) 70%);
  }
  .slogan { z-index: 2; }
  .contact-list { position: absolute; top: 384px; left: 176px; list-style: none; z-index: 2; }
  .contact-list li {
    display: flex; align-items: center; height: 94px;
    color: var(--white); font-size: 42px; letter-spacing: 2.5px; font-weight: 400;
  }
  .contact-list svg { width: 70px; height: 70px; margin-right: 30px; flex: none; }

  .rule-blue { position: absolute; top: 928px; left: 0; width: 100%; height: 14px; background: var(--box-blue); }
  .hours {
    position: absolute; top: 866px; left: 238px; width: 600px; height: 155px;
    background: var(--box-blue); border-radius: 20px; color: var(--white);
    text-align: center; padding-top: 30px; z-index: 2;
  }
  .hours h2 { font-size: 30px; font-weight: 700; letter-spacing: 4px; line-height: 1; margin-bottom: 14px; }
  .hours p { font-size: 24px; font-weight: 600; letter-spacing: 2px; line-height: 1.3; }

  .welcome {
    position: absolute; top: 1040px; left: 0; width: 100%; text-align: center;
    font-size: 96px; font-weight: 700; letter-spacing: 16px; line-height: 1.3;
  }
  .welcome .g { color: var(--brand-green); }
  .welcome .b { color: var(--box-blue); }
</style>
</head>
<body>
<main class="poster">
  <header class="brand">
    <span class="brand-dot"></span>
    <span class="brand-name">
      <span class="word">volora</span>
      <span class="sub">LAUNDRY AND DRY CLEANING</span>
    </span>
  </header>

  <div class="photo" role="img" aria-label="Photograph of an open front-loading washing machine with a grey towel spilling out of the drum"></div>
  <div class="rule-green"></div>
  <div class="slogan">It Comes Back Clean</div>

  <ul class="contact-list">
    <li>
      <svg viewBox="0 0 70 70" aria-hidden="true">
        <path d="M35 4C21 4 11 14 11 27c0 17 24 40 24 40s24-23 24-40C59 14 49 4 35 4z" fill="#fff"/>
        <circle cx="35" cy="27" r="9" fill="#3a3734"/>
      </svg>
      Kwentu-Dasor, Accra
    </li>
    <li>
      <svg viewBox="0 0 70 70" aria-hidden="true">
        <rect x="6" y="6" width="56" height="62" rx="8" fill="#fff"/>
        <path d="M26 18c-4 2-5 6-4 12 2 10 8 19 15 24 4 2 8 2 10-1l-5-8-5 2c-4-4-7-10-8-15l4-3-3-10z" fill="#3a3734"/>
      </svg>
      +233 30 781 6242
    </li>
    <li>
      <svg viewBox="0 0 70 70" aria-hidden="true">
        <rect x="5" y="14" width="60" height="44" fill="none" stroke="#fff" stroke-width="4"/>
        <path d="M5 14l30 26 30-26M5 58l22-22M65 58L43 36" fill="none" stroke="#fff" stroke-width="4"/>
      </svg>
      info@voloralaundry.example
    </li>
    <li>
      <svg viewBox="0 0 70 70" aria-hidden="true" fill="none" stroke="#fff" stroke-width="3">
        <circle cx="35" cy="35" r="30"/>
        <ellipse cx="35" cy="35" rx="13" ry="30"/>
        <path d="M35 5v60M5 35h60M10 20h50M10 50h50"/>
      </svg>
      www.voloralaundry.example
    </li>
  </ul>

  <div class="rule-blue"></div>
  <section class="hours">
    <h2>WORKING HOURS</h2>
    <p>Monday-Saturday<br>8am to 5pm</p>
  </section>

  <h1 class="welcome"><span class="g">W</span><span class="b">E</span><span class="g">L</span><span class="b">C</span><span class="g">O</span><span class="b">M</span><span class="g">E</span></h1>
</main>
</body>
</html>
```